LEARN Business Skills so you can Earn a good living

size of the poster is 8”x 10.75" plus 0.25" bleed.
Please leave 1 inch on the bottoum for footer
I want a design a poster that will attract people's attention.
I appreciate a creative ad however the ad should not take away from being able to clearly read the text.
-I also appreciate a simple creative ad that is not too busy.
-you can use graphics, vectors, or pictures of real people.
-however, if you use real people it should be a white male that is wearing a white shirt and look like a professional person.

Target Market(s)

Potential young business people

Industry/Entity Type

education

Requirements
Must have
• easy to read the text
Nice to have
• I would like a "creative" simple ad that is easy to be read
Should not have
• pictures of women

```html
<!DOCTYPE html>
<html lang="en">
<head>
<meta charset="utf-8">
<title>Learn It to Earn It – Business Enrichment Course</title>
<link href="https://fonts.googleapis.com/css2?family=Alegreya+Sans:wght@500;700;800&family=Oswald:wght@500&display=swap" rel="stylesheet">
<style>
  :root {
    --navy: #0f4686;
    --blue: #1675bf;
    --orange: #f26a21;
    --white: #ffffff;
    --stage: #e9eaec;
    --photo-light: #f6f6f4;
    --photo-mid: #dcd9d3;
  }
  * { margin: 0; padding: 0; box-sizing: border-box; }
  html, body { width: 1200px; height: 900px; overflow: hidden; background: var(--stage); }
  .poster {
    position: absolute; left: 290px; top: 20px;
    width: 620px; height: 860px;
    background: var(--white);
    overflow: hidden;
    font-family: "Alegreya Sans", sans-serif;
  }
  .top-band { position: absolute; left: 0; top: 0; width: 100%; height: 18px; background: var(--blue); }
  .headline { position: absolute; left: 0; top: 0; width: 620px; height: 240px; }
  .headline text { font-family: "Alegreya Sans", sans-serif; font-weight: 800; }
  .headline .word { fill: var(--navy); font-size: 128px; }
  .headline .accent { fill: var(--orange); font-size: 128px; }
  .headline .joiner { fill: var(--orange); font-size: 56px; font-weight: 500; }
  .course-band {
    position: absolute; left: 0; top: 237px; width: 100%; height: 55px;
    background: var(--blue); color: var(--white);
    font-weight: 700; font-size: 47px; line-height: 53px;
    text-align: center; white-space: nowrap;
  }
  .promise-band {
    position: absolute; left: 55px; top: 292px; width: 510px; height: 53px;
    background: var(--orange);
  }
  .promise-band text, .goals text {
    font-family: "Oswald", sans-serif; font-weight: 500; text-transform: uppercase;
  }
  .promise-band text { fill: var(--white); font-size: 20px; }
  .skills-title {
    position: absolute; left: 42px; top: 348px;
    color: var(--navy); font-weight: 800; font-size: 52px; line-height: 44px;
    white-space: nowrap;
  }
  .rule { position: absolute; left: 0; height: 2px; background: var(--navy); }
  .rule-title { top: 449px; width: 468px; }
  .rule-goals { top: 506px; width: 386px; }
  .rule-footer { top: 784px; width: 100%; height: 3px; }
  .goals { position: absolute; left: 0; top: 455px; width: 420px; height: 52px; }
  .goals text { fill: var(--orange); }
  .goals .main { font-size: 24px; }
  .goals .sub { font-size: 20px; }
  .topics { position: absolute; z-index: 2; list-style: none; color: var(--navy);
    font-weight: 700; font-size: 15px; line-height: 22.3px; text-transform: uppercase; letter-spacing: 0.2px; }
  .topics li { position: relative; padding-left: 11px; white-space: nowrap; }
  .topics li::before { content: ""; position: absolute; left: 0; top: 6px; width: 6px; height: 6px; border-radius: 50%; background: var(--orange); }
  .topics-left { left: 45px; top: 516px; }
  .topics-right { left: 220px; top: 561px; }
  .portrait {
    position: absolute; z-index: 1; left: 430px; top: 396px; width: 190px; height: 388px;
    background: linear-gradient(180deg, var(--photo-light) 0%, var(--photo-mid) 100%);
  }
</style>
</head>
<body>
  <main class="poster">
    <div class="top-band"></div>

    <svg class="headline" viewBox="0 0 620 240" aria-label="Learn it to earn it">
      <text class="word" x="53" y="132" textLength="374" lengthAdjust="spacingAndGlyphs">LEARN</text>
      <text class="accent" x="477" y="132" textLength="101" lengthAdjust="spacingAndGlyphs">IT</text>
      <text class="joiner" x="66" y="187">to</text>
      <text class="word" x="129" y="229" textLength="298" lengthAdjust="spacingAndGlyphs">EARN</text>
      <text class="accent" x="475" y="229" textLength="96" lengthAdjust="spacingAndGlyphs">IT</text>
    </svg>

    <div class="course-band">Business Enrichment Course</div>

    <svg class="promise-band" viewBox="0 0 510 53">
      <text x="255" y="34" text-anchor="middle" textLength="462" lengthAdjust="spacingAndGlyphs">A proven success of helping people in their livelihoods</text>
    </svg>

    <h2 class="skills-title">Business skills that<br>will help you:</h2>
    <div class="rule rule-title"></div>

    <svg class="goals" viewBox="0 0 420 52">
      <text class="main" x="40" y="34" textLength="157" lengthAdjust="spacingAndGlyphs">Get a quality job</text>
      <text class="sub" x="203" y="21" textLength="210" lengthAdjust="spacingAndGlyphs">- Start/Grow your business</text>
      <text class="sub" x="203" y="45" textLength="173" lengthAdjust="spacingAndGlyphs">- Increase your salary</text>
    </svg>
    <div class="rule rule-goals"></div>

    <ul class="topics topics-left">
      <li>Business Admiistration</li>
      <li>Small Business Management</li>
      <li>Finance</li>
      <li>Computers</li>
      <li>Sales&nbsp; Marketing</li>
      <li>Interviewing Skills</li>
      <li>Negotiation</li>
      <li>Import/Export</li>
      <li>Distribution</li>
      <li>LedgerPro</li>
      <li>Health Care</li>
      <li>Marketly</li>
    </ul>
    <ul class="topics topics-right">
      <li>Investments</li>
      <li>Accounting</li>
      <li>Project Management</li>
      <li>Business Law</li>
      <li>Public Speaking</li>
      <li>Information Technoloy</li>
      <li>Marketing</li>
      <li>Real Estate</li>
      <li>Management</li>
    </ul>

    <div class="portrait" role="img" aria-label="Photo of a smiling young professional man in a white shirt pointing at the course list"></div>
    <div class="rule rule-footer"></div>
  </main>
</body>
</html>
```